Wealth Management Business Card

We are a professional services consulting firm that specializes in high net worth individuals over $25,000,000, executives C-suite and above, closely held businesses owners, family offices and highly compensated employees.

Our focus is on risk mitigation and tax efficient strategies. Our clients take their risk on themselves and have a proven track record generating wealth. Our directive is to preserve and protect the wealth they’ve already created.

Our company Harbridge Advisory is geared around five directives of asset protection:
1) Legal Structuring
2) Leverage & Financing
3) Risk Management - Asset Protection & Insurance, Trustee Work
4) Asset Management & Investing - Under www.qelvantcapital.com
5) Tax Efficient Strategies

Our Company Mark is a Pentagon with a key in the middle. A pentagon is the most efficient defensive structure. Each point of a pentagon is equal distance front every point . Each side provides support to another and works together, which is the key to our clients success.

Our key colors are blue, black and silver.

We ‘re located in the Pacific Northwest with bi coastal and international clients. We have fewer, higher net worth clients and provide exceptional customer service. We do not do social media.

website is www.harbridgepath.com

Target Market(s)

High End Clients

Contact Information for Business Card

extra thick

Font styles to use
Serif

Requirements
Must have
• Metalic foil for lettering.
Black Background on one side
White Background on the other
Horizontal Format Only
No Rounded corners
Not Marketing sales information on the card.
Nice to have
• imprinted texture on the card
Should not have
• lots of color

```html
<!DOCTYPE html>
<html lang="en">
<head>
<meta charset="utf-8">
<title>Harbridge Advisory — Business Card</title>
<link rel="stylesheet" href="https://fonts.googleapis.com/css2?family=Cinzel:wght@400&family=Poppins:wght@300;400;600&display=swap">
<style>
  :root {
    --backdrop: #1b1b1d;
    --card-white: #ffffff;
    --card-black: #0b0b0c;
    --navy: #12296b;
    --accent-blue: #2a7fd4;
    --ink: #3c3f4a;
    --silver: #a9adb4;
    --pattern-top: #3a3b3f;
    --pattern-bottom: #0d0d0f;
  }
  * { box-sizing: border-box; margin: 0; padding: 0; }
  html, body {
    width: 1200px; height: 960px; overflow: hidden;
    background: var(--backdrop);
  }
  .stage { position: relative; width: 1200px; height: 960px; }

  .card {
    position: absolute;
    width: 660px; height: 378px;
    box-shadow: 0 18px 40px rgba(0,0,0,.55);
    overflow: hidden;
  }

  /* Back: black card, top right */
  .card-back { left: 470px; top: 70px; background: var(--card-black); }
  .back-pattern {
    position: absolute; inset: 0;
    background: linear-gradient(160deg, var(--pattern-top), var(--pattern-bottom) 70%);
  }
  .back-brand {
    position: absolute; left: 50%; top: 50%;
    transform: translate(-50%, -50%);
    display: flex; align-items: center; gap: 10px;
  }
  .back-brand-square { width: 18px; height: 18px; background: var(--accent-blue); }
  .back-brand-name {
    font-family: "Cinzel", serif; font-weight: 400;
    color: var(--silver); font-size: 16px; letter-spacing: 1px;
    white-space: nowrap;
  }

  /* Front: white card, bottom left, landscape */
  .card-front { left: 70px; top: 510px; background: var(--card-white); }
  .brand {
    position: absolute; left: 48px; top: 56px;
    display: flex; align-items: center; gap: 18px;
  }
  .brand-square { width: 48px; height: 48px; background: var(--navy); flex: none; }
  .brand-name {
    font-family: "Cinzel", serif; font-weight: 400;
    color: var(--navy); font-size: 30px; line-height: 1.1;
    letter-spacing: 1px; white-space: nowrap;
  }
  .contact {
    position: absolute; left: 330px; bottom: 40px; width: 300px;
    font-family: "Poppins", sans-serif; color: var(--ink);
  }
  .person-name {
    font-weight: 600; color: var(--navy);
    font-size: 17px; letter-spacing: .5px; text-transform: uppercase;
    white-space: nowrap;
  }
  .person-role { font-weight: 300; font-size: 14px; margin-bottom: 18px; }
  .address { font-weight: 300; font-size: 13px; line-height: 1.5; margin-bottom: 14px; white-space: nowrap; }
  .contact-list { list-style: none; font-weight: 300; font-size: 13px; line-height: 1.65; }
  .contact-list li { display: flex; align-items: center; gap: 8px; white-space: nowrap; }
  .contact-list svg { width: 12px; height: 12px; flex: none; }
</style>
</head>
<body>
<main class="stage">
  <section class="card card-back">
    <div class="back-pattern" role="img" aria-label="Repeating embossed geometric foil pattern across the black card"></div>
    <div class="back-brand">
      <div class="back-brand-square"></div>
      <span class="back-brand-name">Harbridge Advisory</span>
    </div>
  </section>

  <section class="card card-front">
    <div class="brand">
      <div class="brand-square"></div>
      <div class="brand-name">Harbridge<br>Advisory</div>
    </div>
    <div class="contact">
      <p class="person-name">Corwin Ashby</p>
      <p class="person-role">Founder</p>
      <p class="address">418 Alder Ridge Rd, Suite 112<br>Westlake, OR 97120</p>
      <ul class="contact-list">
        <li>
          <svg viewBox="0 0 16 16"><rect x="2" y="1" width="12" height="14" rx="2" fill="none" stroke="#12296b" stroke-width="1.8"/><path d="M6 5c0 3 2 6 5 6" fill="none" stroke="#12296b" stroke-width="1.6"/></svg>
          (503) 555-0147
        </li>
        <li>
          <svg viewBox="0 0 16 16"><rect x="1" y="3" width="14" height="10" fill="#12296b"/><path d="M1 3l7 6 7-6" fill="none" stroke="#fff" stroke-width="1.2"/></svg>
          info@harbridgepath.com
        </li>
        <li>
          <svg viewBox="0 0 16 16"><circle cx="8" cy="8" r="7" fill="#12296b"/><ellipse cx="8" cy="8" rx="3" ry="7" fill="none" stroke="#fff" stroke-width="1"/><path d="M1 8h14" stroke="#fff" stroke-width="1"/></svg>
          www.harbridgepath.com
        </li>
      </ul>
    </div>
  </section>
</main>
</body>
</html>
```